Business Card for Financial Asset Management Company

Now we are launching a new company based in Tokyo.
The company information is below;

Company Name: Talvane Management

Operations: Financial assets management, Proposing forming portfolio of assets, Consulting service, and advising to enhance your company's financial health

Corporate Colour: Japan Blue or Navy like below
http://staffpages.qorvenly.edu/mtavis/images/Slate/Teal-Slate-217.jpg

It's dark and deep, and will get to fit to our clients as our relationships last longer and longer.

Our images for this colour are "Japanese style" and "pride in our craftmanship" , and also "gentle".

Corporate Key Image: an order taker who is sincere, polite, but courageous

We don't have our logo yet so please feel free to put any symbol on your design.

Please do not hesitate about asking any questions.
Thank you :-)

Reason: We are still discussin on final decision. Thank you for your understanding.

```html
<!DOCTYPE html>
<html lang="en">
<head>
<meta charset="utf-8">
<title>Talvane Management – Business Card</title>
<link rel="stylesheet" href="https://fonts.googleapis.com/css2?family=Arimo:wght@400;700&family=Open+Sans:wght@400&display=swap">
<style>
  :root {
    --stage: #d9d9db;
    --navy: #232a7a;
    --navy-deep: #0c0d2e;
    --navy-mid: #1c1f66;
    --ink: #0d0d12;
    --lavender: #b9b6e6;
    --lavender-soft: #ebeaf9;
    --ring: #5a55b8;
    --steel: #d3d5df;
    --bullet: #e0663a;
    --copy: #6a6a80;
    --white: #ffffff;
  }
  * { box-sizing: border-box; margin: 0; padding: 0; }
  html, body {
    width: 1200px; height: 960px; overflow: hidden;
    background: var(--stage);
  }
  .stage {
    position: relative; width: 1200px; height: 960px;
  }
  .card {
    position: absolute; top: 320px;
    width: 520px; height: 300px; overflow: hidden;
    box-shadow: 0 8px 24px rgba(0,0,0,.25);
  }

  /* Front card */
  .card--front { left: 50px; background: var(--white); }
  .card--front .sphere { position: absolute; inset: 0; }
  .front__name {
    position: absolute; left: 40px; top: 118px;
    font-family: "Arimo", Arial, sans-serif; font-weight: 700;
    line-height: 1.02; letter-spacing: .5px;
  }
  .front__name .line-one { display: block; color: var(--navy); font-size: 25px; }
  .front__name .line-two { display: block; color: var(--ink); font-size: 25px; }
  .front__mark {
    position: absolute; left: 268px; top: 62px;
    display: flex; align-items: center; gap: 8px;
    font-family: "Arimo", Arial, sans-serif; font-weight: 700;
    font-size: 17px; color: var(--navy); letter-spacing: .3px;
  }
  .front__mark .square { width: 14px; height: 14px; background: var(--navy); }
  .services {
    position: absolute; left: 262px; top: 200px;
    list-style: none;
    font-family: "Open Sans", Arial, sans-serif; font-size: 10px;
    color: var(--copy); line-height: 16px;
  }
  .services li { position: relative; padding-left: 10px; }
  .services li::before {
    content: ""; position: absolute; left: 0; top: 6px;
    width: 5px; height: 5px; border-radius: 50%; background: var(--bullet);
  }

  /* Back card */
  .card--back {
    left: 630px;
    background: linear-gradient(160deg, var(--navy-deep) 0%, var(--navy-mid) 45%, var(--navy) 70%, var(--navy-deep) 100%);
  }
  .card--back .swoosh { position: absolute; inset: 0; }
  .back__mark {
    position: absolute; left: 0; right: 0; top: 112px;
    display: flex; flex-direction: column; align-items: center; gap: 12px;
    font-family: "Arimo", Arial, sans-serif; font-weight: 700;
    color: var(--steel); text-transform: uppercase;
  }
  .back__mark .square { width: 26px; height: 26px; background: var(--steel); }
  .back__mark .name { font-size: 22px; letter-spacing: 2px; text-align: center; line-height: 1.1; }
</style>
</head>
<body>
<main class="stage">

  <section class="card card--front" aria-label="Business card front">
    <svg class="sphere" width="520" height="300" viewBox="0 0 520 300" aria-hidden="true">
      <defs>
        <radialGradient id="sphere-fill" cx="0.45" cy="0.35" r="0.7">
          <stop offset="0" stop-color="#ffffff"/>
          <stop offset="0.55" stop-color="#e4e2f6"/>
          <stop offset="1" stop-color="#aaa6de"/>
        </radialGradient>
      </defs>
      <path d="M380 30 A150 150 0 0 1 520 120 L520 60 A170 170 0 0 0 420 18 Z" fill="var(--ring)" opacity=".75"/>
      <circle cx="390" cy="165" r="150" fill="url(#sphere-fill)"/>
      <rect x="0" y="268" width="230" height="32" fill="var(--navy)"/>
      <rect x="0" y="278" width="205" height="22" fill="var(--ink)"/>
    </svg>
    <div class="front__name">
      <span class="line-one">TALVANE</span>
      <span class="line-two">MANAGEMENT</span>
    </div>
    <div class="front__mark"><span class="square"></span>Talvane</div>
    <ul class="services">
      <li>Financial Assets Management</li>
      <li>Proposing forming portfolio of assets</li>
      <li>Consulting service</li>
      <li>Advising to enhance your company's financial health</li>
    </ul>
  </section>

  <section class="card card--back" aria-label="Business card back">
    <svg class="swoosh" width="520" height="300" viewBox="0 0 520 300" aria-hidden="true">
      <defs>
        <linearGradient id="swoosh-fill" x1="0" y1="0" x2="1" y2="0">
          <stop offset="0" stop-color="#3a3fb0" stop-opacity="0"/>
          <stop offset="0.5" stop-color="#3d43c0" stop-opacity=".75"/>
          <stop offset="1" stop-color="#2b2f95" stop-opacity=".2"/>
        </linearGradient>
      </defs>
      <path d="M0 60 C140 20 300 40 520 90 L520 120 C320 70 150 60 0 95 Z" fill="url(#swoosh-fill)" opacity=".55"/>
      <path d="M60 250 C200 200 360 210 520 240 L520 262 C360 232 220 232 80 275 Z" fill="url(#swoosh-fill)"/>
    </svg>
    <div class="back__mark">
      <span class="square"></span>
      <span class="name">Talvane<br>Management</span>
    </div>
  </section>

</main>
</body>
</html>
```